Letterhead to Prospective Clients

Create a letterhead (word & canva) that I will use to send letters to prospective clients and also include the Harbourline Estate Group Logo, My Contact Details and Interchangeable "Suburb". Use the same font and colour pallete

Maris Toppel | "Suburb" Specialist - Redlands & Surrounds
Mobile: 0417 862 905
Email: MT@HarbourlineEstateGroup.com.au

```html
<!DOCTYPE html>
<html lang="en">
<head>
<meta charset="utf-8">
<title>Harbourline Estate Group – Letterhead</title>
<link href="https://fonts.googleapis.com/css2?family=Montserrat:wght@300;500;600&display=swap" rel="stylesheet">
<style>
  :root {
    --navy: #02143a;
    --tan: #d4a67a;
    --ink: #111111;
    --paper: #ffffff;
    --backdrop: #cdd3d3;
  }
  * { margin: 0; padding: 0; box-sizing: border-box; }
  html, body {
    width: 1200px;
    height: 1028px;
    overflow: hidden;
    background: var(--backdrop);
    font-family: "Montserrat", sans-serif;
  }
  .letterhead {
    position: absolute;
    left: 267px;
    top: 44px;
    width: 666px;
    height: 940px;
    background: var(--paper);
  }
  .brand-name {
    position: absolute;
    left: 34px;
    top: 60px;
    font-weight: 300;
    font-size: 15px;
    letter-spacing: 3px;
    text-transform: uppercase;
    color: var(--navy);
    white-space: nowrap;
  }
  .agent {
    position: absolute;
    right: 36px;
    top: 33px;
    text-align: right;
  }
  .agent-name {
    font-weight: 600;
    font-size: 31px;
    line-height: 34px;
    color: var(--tan);
  }
  .agent-role {
    margin-top: 2px;
    font-weight: 500;
    font-size: 11.5px;
    letter-spacing: 0.3px;
    color: var(--ink);
  }
  .contact-list {
    list-style: none;
    margin-top: 10px;
  }
  .contact-item {
    display: flex;
    justify-content: flex-end;
    align-items: center;
    gap: 8px;
    font-weight: 500;
    font-size: 11.5px;
    line-height: 16px;
    letter-spacing: 0.3px;
    color: var(--ink);
  }
  .contact-icon { width: 11px; height: 11px; }
  .header-rule {
    position: absolute;
    top: 136px;
    left: 35px;
    width: 596px;
    height: 2px;
    display: flex;
  }
  .header-rule .rule-navy { flex: 1; background: var(--navy); }
  .header-rule .rule-tan { flex: 1; background: var(--tan); }
  .footer-bands {
    position: absolute;
    left: 0;
    bottom: 0;
    width: 666px;
    height: 30px;
  }
</style>
</head>
<body>
  <main class="letterhead">
    <div class="brand-name">Harbourline Estate Group</div>

    <section class="agent">
      <h1 class="agent-name">Maris Toppel</h1>
      <p class="agent-role">"Suburb" Specialist - Redlands &amp; Surrounds</p>
      <ul class="contact-list">
        <li class="contact-item">
          <span>0417 862 905</span>
          <svg class="contact-icon" viewBox="0 0 24 24" aria-hidden="true">
            <path d="M6.6 10.8a15.1 15.1 0 0 0 6.6 6.6l2.2-2.2a1 1 0 0 1 1-.25 11.4 11.4 0 0 0 3.6.57 1 1 0 0 1 1 1V20a1 1 0 0 1-1 1A17 17 0 0 1 3 4a1 1 0 0 1 1-1h3.5a1 1 0 0 1 1 1c0 1.25.2 2.45.57 3.57a1 1 0 0 1-.25 1z" fill="none" stroke="var(--tan)" stroke-width="2"/>
          </svg>
        </li>
        <li class="contact-item">
          <span>MT@HarbourlineEstateGroup.com.au</span>
          <svg class="contact-icon" viewBox="0 0 24 24" aria-hidden="true">
            <rect x="2" y="6" width="20" height="15" fill="none" stroke="var(--tan)" stroke-width="2"/>
            <path d="M2 7l10 7 10-7" fill="none" stroke="var(--tan)" stroke-width="2"/>
          </svg>
        </li>
      </ul>
    </section>

    <div class="header-rule"><span class="rule-navy"></span><span class="rule-tan"></span></div>

    <svg class="footer-bands" viewBox="0 0 666 30" preserveAspectRatio="none" aria-hidden="true">
      <polygon points="0,0 348,0 300,19 0,19" fill="var(--navy)"/>
      <polygon points="348,12 666,12 666,30 304,30" fill="var(--tan)"/>
    </svg>
  </main>
</body>
</html>
```